Vemko Whitepaper - PDF/JPEG one page 'front cover' design for Vemko 'Whitepaper' document.

Single page front page design (as PDF/JPEG) modelled on PlumeTrux example.

Target Market(s)

Venture capitalists

Industry/Entity Type

Crypto

Font styles to use
Sans Serif

Colors
A7469A
B969AE
D3A5CF
EDDBEB
F8F0F9

Requirements
Must have
• Contemporary 'crypto' design. Text should say "Vemko Whitepaper" at top, split onto two lines like the PlumeTrux example. And "October 2021
Nice to have
• I like the example from PLUMETRUX that I attached.

```html
<!DOCTYPE html>
<html lang="en">
<head>
<meta charset="utf-8">
<title>Vemko Whitepaper – Front Cover</title>
<link rel="stylesheet" href="https://fonts.googleapis.com/css2?family=Open+Sans:wght@700&family=Orbitron:wght@400;800&display=swap">
<style>
  :root {
    --stage: #e4e4e6;
    --cover-maroon: #8b003f;
    --cover-charcoal: #2e2e2e;
    --cover-white: #ffffff;
    --brand-pink: #ee2a7b;
  }
  html, body {
    margin: 0;
    padding: 0;
    width: 1040px;
    height: 1200px;
    overflow: hidden;
    background: var(--stage);
  }
  .canvas {
    position: relative;
    width: 1040px;
    height: 1200px;
    display: flex;
    justify-content: center;
    align-items: center;
  }
  .cover {
    display: block;
    width: 932px;
    height: 1200px;
  }
  .cover-base { fill: var(--cover-maroon); }
  .cover-band { fill: var(--cover-charcoal); }
  .band-edge { fill: none; stroke: var(--cover-white); stroke-width: 5; stroke-linejoin: round; }
  .top-glow { fill: var(--cover-white); }
  .brand-mark { fill: var(--brand-pink); stroke: var(--cover-charcoal); stroke-width: 3; }
  .brand-name {
    font-family: "Open Sans", Arial, sans-serif;
    font-weight: 700;
    font-size: 60px;
    fill: var(--cover-charcoal);
  }
  .title-main {
    font-family: "Orbitron", "Arial Black", sans-serif;
    font-weight: 800;
    font-size: 110px;
    fill: var(--cover-white);
  }
  .title-sub {
    font-family: "Orbitron", Arial, sans-serif;
    font-weight: 400;
    font-size: 48px;
    fill: var(--cover-white);
  }
  .issue-date {
    font-family: "Orbitron", Arial, sans-serif;
    font-weight: 400;
    font-size: 34px;
    fill: var(--cover-white);
  }
</style>
</head>
<body>
<main class="canvas">
  <svg class="cover" viewBox="0 0 932 1200" xmlns="http://www.w3.org/2000/svg" aria-labelledby="cover-title">
    <title id="cover-title">Vemko Whitepaper, October 2021</title>
    <defs>
      <filter id="glow-blur" x="-30%" y="-30%" width="160%" height="160%">
        <feGaussianBlur stdDeviation="28"/>
      </filter>
      <clipPath id="band-clip">
        <polygon points="0,0 932,0 932,186 466,842 0,216"/>
      </clipPath>
    </defs>

    <rect class="cover-base" x="0" y="0" width="932" height="1200"/>

    <g class="top-band">
      <polygon class="cover-band" points="0,0 932,0 932,186 466,842 0,216"/>
      <g clip-path="url(#band-clip)">
        <polygon class="top-glow" filter="url(#glow-blur)" points="220,-40 720,-40 600,140 470,200 340,140"/>
      </g>
      <polyline class="band-edge" points="0,216 466,842 932,186"/>
    </g>

    <g class="brand">
      <circle class="brand-mark" cx="364" cy="80" r="13"/>
      <text class="brand-name" x="392" y="101">Vemko</text>
    </g>

    <g class="cover-title">
      <text class="title-main" x="240" y="342" textLength="452" lengthAdjust="spacingAndGlyphs">VEMKO</text>
      <text class="title-sub" x="240" y="398" textLength="452" lengthAdjust="spacingAndGlyphs">WHITEPAPER</text>
    </g>

    <text class="issue-date" x="261" y="1143" textLength="411" lengthAdjust="spacingAndGlyphs">OCTOBER 2021</text>
  </svg>
</main>
</body>
</html>
```